Dean wants a Kick arse Business card

Launching my new company Harrow Real Estate 1st July, and will be mailing out to past clients, need a kick arse business card design pronto to get printing done in time for mail out
I'm after a two sided card - one side for all contact details (see below) the other side for impact (kick arsery!)
Logo and my photo attached, details to go onto card are as follows
Dean Harrow - Principal
M: 0412 905 364
E: dean@harrowre.com.au
Dean Harrow Real Estate Pty Ltd trading as Harrow Real Estate
Licensed Real Estate & Business Agents
ABN 42 803 517 296 Triennial Cert No. RA31472
14 Marbrook Avenue, Kelmscott WA 6111
Tel: 08 9371 6048 Fax: 08 6209 4812

```html
<!DOCTYPE html>
<html lang="en">
<head>
<meta charset="utf-8">
<title>Harrow Real Estate – Business Card</title>
<link rel="stylesheet" href="https://fonts.googleapis.com/css2?family=Arimo:wght@400;700&family=Fjalla+One&display=swap">
<style>
  :root {
    --page: #ffffff;
    --card-edge: #3a9ccf;
    --navy: #0d3550;
    --navy-deep: #062a3d;
    --teal: #0e6a93;
    --sky: #5aace0;
    --slate: #3e5479;
    --mist: #cbd4e3;
    --ink: #111a2c;
    --brand: #0f5f8f;
  }
  * { margin: 0; padding: 0; box-sizing: border-box; }
  html, body { width: 1200px; height: 1000px; overflow: hidden; background: var(--page); }
  .canvas { position: relative; width: 1200px; height: 1000px; }

  .card { position: absolute; overflow: hidden; border: 1px solid var(--card-edge); background: #fff; }
  .card-front { left: 279px; top: 50px; width: 642px; height: 416px; }
  .card-back  { left: 278px; top: 532px; width: 643px; height: 417px; }
  .card svg.backdrop { position: absolute; left: 0; top: 0; }

  .brand { position: absolute; display: flex; align-items: center; gap: 8px;
           font-family: "Arimo", Arial, sans-serif; font-weight: 700; color: var(--brand); white-space: nowrap; }
  .brand-dot { border-radius: 50%; background: var(--brand); flex: none; }
  .card-front .brand { left: 14px; top: 92px; font-size: 25px; }
  .card-front .brand-dot { width: 30px; height: 30px; }
  .card-back .brand { left: 462px; top: 52px; font-size: 16px; }
  .card-back .brand-dot { width: 20px; height: 20px; }

  .agent { position: absolute; left: 265px; top: 126px; font-family: "Fjalla One", "Arial Narrow", sans-serif;
           font-size: 12.5px; line-height: 18px; color: var(--ink); letter-spacing: 0.2px; }
  .company { position: absolute; left: 265px; top: 252px; font-family: "Arimo", Arial, sans-serif;
             font-size: 13.4px; line-height: 23.4px; color: var(--ink); }
</style>
</head>
<body>
<div class="canvas">

  <section class="card card-front">
    <svg class="backdrop" width="642" height="416" viewBox="0 0 642 416">
      <defs>
        <linearGradient id="front-sweep" x1="0" y1="0" x2="0" y2="1">
          <stop offset="0" stop-color="#5aace0"/>
          <stop offset="1" stop-color="#3e5479"/>
        </linearGradient>
      </defs>
      <circle cx="600" cy="360" r="250" fill="url(#front-sweep)"/>
    </svg>
    <div class="brand"><span class="brand-dot"></span>Harrow Real Estate</div>
  </section>

  <section class="card card-back">
    <svg class="backdrop" width="643" height="417" viewBox="0 0 643 417">
      <defs>
        <linearGradient id="top-band" x1="0" y1="0" x2="0" y2="1">
          <stop offset="0" stop-color="#062a3d"/>
          <stop offset="1" stop-color="#0e6a93"/>
        </linearGradient>
        <linearGradient id="info-panel" x1="0" y1="0" x2="0" y2="1">
          <stop offset="0" stop-color="#ffffff"/>
          <stop offset="1" stop-color="#9cc3e6"/>
        </linearGradient>
        <linearGradient id="corner" x1="0" y1="0" x2="0" y2="1">
          <stop offset="0" stop-color="#0e6a93"/>
          <stop offset="1" stop-color="#062a3d"/>
        </linearGradient>
        <linearGradient id="portrait" x1="0" y1="0" x2="0" y2="1">
          <stop offset="0" stop-color="#8a8f96"/>
          <stop offset="0.5" stop-color="#3b3f45"/>
          <stop offset="1" stop-color="#1c1f24"/>
        </linearGradient>
        <filter id="lift" x="-10%" y="-10%" width="120%" height="120%">
          <feDropShadow dx="0" dy="-2" stdDeviation="3" flood-color="#000" flood-opacity="0.55"/>
        </filter>
      </defs>
      <rect width="643" height="417" fill="url(#top-band)"/>
      <path d="M0 110 Q260 0 643 8 L643 417 L0 417 Z" fill="#ffffff"/>
      <path d="M0 110 Q90 62 195 40 Q420 160 540 417 L0 417 Z" fill="var(--mist)"/>
      <rect role="img" aria-label="Portrait photo of Dean Harrow" x="0" y="95" width="222" height="322" rx="0" fill="url(#portrait)"/>
      <path d="M175 417 Q260 190 470 182 Q590 182 643 240 L643 417 Z" fill="url(#info-panel)" filter="url(#lift)"/>
      <path d="M643 300 Q560 380 420 417 L643 417 Z" fill="url(#corner)"/>
    </svg>

    <div class="brand"><span class="brand-dot"></span>Harrow Real Estate</div>

    <div class="agent">
      <div>Dean Harrow - Principal</div>
      <div>M: 0412 905 364</div>
      <div>E: dean@harrowre.com.au</div>
    </div>

    <div class="company">
      <div>Dean Harrow Real Estate Pty Ltd trading as Harrow Real Estate</div>
      <div>Licensed Real Estate &amp; Business Agents</div>
      <div>ABN 42 803 517 296 Triennial Cert No. RA31472</div>
      <div>14 Marbrook Avenue, Kelmscott WA 6111</div>
      <div>Tel: 08 9371 6048 Fax: 08 6209 4812</div>
    </div>
  </section>

</div>
</body>
</html>
```